Curavel - Ensuring better transparency in where drugs are made.

I am developing a consumer advocacy organization called Curavel that is looking at creating a site specifically around better transparency in where your medications are being manufactured. This is a very important topic for me as I am a pharmacist and understand the negative down stream impacts of poor quality in the pharmacy supply chain. Almost every consumer that is prescribed medications likely has no idea about the intricacies behind how their medications reach the shelf in their pharmacies. And most would be shock to understand how many different components have impact on the quality. I have intimate knowledge of this space as I currently oversee all contracting for the third largest GPO in the country. My team manages $10B in pharmaceutical spend and understanding the supply chains for the largest Pharma manufactures in the world is very complex. Below is a article that my team put together about the problem and our solution. Curavel - Is a consumer advocacy organization created to provide more transparency on where your drugs are manufactured.

Where are your drugs made?
Prescription drugs sold in the U.S. are manufactured in facilities located all over the world. Many medications you rely on are made in Australia, Canada, China, India, France, Germany, Japan, Malta, Singapore, Sweden, the United Kingdom, and the United States. Unfortunately, if you live in the U.S., and other countries as well, it can be quite the task to pinpoint exactly where your medication was made because companies are not required to list that information.In fact, drug companies are only required to list the corporate headquarters on the label, but the actual manufacturing facility and its location are usually elsewhere. Complicating matters even more, many pharmaceutical companies, such as Orvan Tesk, BrennerHollowayCo, Dravo, and Kolvat, often use contract manufacturers. This means the company distributing the medication is not the one that manufactured it. Curavel has researched where some of the most popular drugs in the U.S. are made. In the U.S., many brand-name drugs' packaging includes where the drug is made. We have found that 70% of popular brand-name drugs sold in U.S. pharmacies are imported.We've found that some countries are more transparent than others. In Canada, the label often does not specify where the drug is made, but it almost always does on packaging in Turkey.In terms of your safety, wherever the manufacturing location, it is crucial to your health that you take lawfully and properly-manufactured drugs.Oversight in the U.S.Regardless of where they are made, drugs sold in the United States must comply with BMR's rules, which require that drugs are made in accordance with good manufacturing practices to assure quality, and that products are labeled properly to help you safely use them. Domestic and foreign manufacturing plants that manufacture medications for distribution in the U.S. are usually but not always inspected for compliance with BMR regulations (Source: National Civic Review Bureau).Oversight in Canada and Other Highly-developed CountriesAlthough requirements vary across different countries, the most economically advanced countries usually have similar regulations to the U.S. when it comes to manufacturing. For example, Canadians count on their government to regulate medications approved for sale in Canada through Welfare Board's Remedy Standards Division, Canada's equivalent to the U.S. BMR. It's important to note that the U.S. recognizes 25 countries (including Australia, Canada, New Zealand, United Kingdom) as having comparable regulatory oversight as well as pharmaceutical regulatory systems comparable in sophistication and stringency to that of the U.S. This is a premise widely supported by the BMR and American pharmaceutical industry. Many medications sold in those countries are actually made in the U.S.The bottom line is that it is not always easy to determine where a product is manufactured. Your pharmacist is an excellent source for information regarding the medication that he/she dispenses, but we also encourage people to take control of their health and do their own research! Let Curavel help you better understand where your drugs are actually made and the quality of the manufacturing involved.

Target Market(s)

Anyone taking medications.

Industry/Entity Type

Health Care

Logo Text

Curavel

Coding

Coded - Design and coding required

Number of Pages Required

3 page

Colors

Designer to choose colors to be used in the design.

```html
<!DOCTYPE html>
<html lang="en">
<head>
<meta charset="utf-8">
<title>Curavel – Where Are Your Drugs Made?</title>
<link rel="stylesheet" href="https://fonts.googleapis.com/css2?family=Raleway:wght@300;400;600;700;800&family=Open+Sans:wght@400;600&family=Montserrat:wght@400;600;700&display=swap">
<style>
:root{
  --blue:#1ba5e8;
  --teal:#1db3ad;
  --teal-dark:#12a09f;
  --green:#8cc63f;
  --ink:#222428;
  --text:#5b5e63;
  --light:#f3f4f8;
  --dark:#141414;
  --darker:#0d0d0d;
  --white:#ffffff;
}
*{box-sizing:border-box;margin:0;padding:0}
html,body{width:1200px;height:4521px;overflow:hidden}
body{font-family:"Open Sans",sans-serif;color:var(--text);background:var(--white);position:relative}
.abs{position:absolute}
svg{display:block}

/* header */
.site-header{position:absolute;top:0;left:0;width:1200px;height:117px;background:var(--white)}
.topbar{position:absolute;left:415px;top:0;width:785px;height:38px;background:var(--blue);clip-path:polygon(0 0,100% 0,100% 100%,36px 100%);color:#fff;font-family:"Montserrat",sans-serif;font-size:15px;display:flex;align-items:center;gap:30px;padding-left:100px}
.topbar .item{display:flex;align-items:center;gap:8px}
.topbar .socials{display:flex;gap:6px}
.topbar .socials span{width:24px;height:24px;border:1.5px solid #fff;border-radius:50%}
.brand{position:absolute;left:148px;top:38px;display:flex;align-items:center;gap:14px}
.brand .mark{width:52px;height:52px;border-radius:8px;background:var(--teal)}
.brand .name{font-family:"Raleway",sans-serif;font-weight:800;font-size:38px;color:var(--green)}
.main-nav{position:absolute;top:68px;left:441px;display:flex;gap:28px;font-family:"Raleway",sans-serif;font-weight:700;font-size:15px;color:var(--ink)}

/* hero */
.hero{position:absolute;top:117px;left:0;width:1200px;height:633px;background:linear-gradient(100deg,#2e3440 0%,#6b7486 35%,#b7bfcd 65%,#d7dde6 100%)}
.hero-copy{position:absolute;left:142px;top:150px;color:#fff}
.hero-copy .pre{font-family:"Raleway",sans-serif;font-weight:300;font-size:40px;letter-spacing:1px}
.hero-copy h1{font-family:"Raleway",sans-serif;font-weight:800;font-size:64px;line-height:1;margin-top:2px}
.hero-copy p{font-size:16px;line-height:27px;width:400px;margin-top:22px}
.btn-blue{display:inline-block;margin-top:30px;background:var(--blue);color:#fff;font-family:"Montserrat",sans-serif;font-weight:600;font-size:14px;padding:12px 22px}
.hero .arrow{position:absolute;top:295px;width:30px;height:30px;border-radius:50%;background:rgba(0,0,0,.55)}
.hero-bottom-chevron{position:absolute;left:585px;top:738px}

/* origin section */
.origin{position:absolute;top:750px;left:0;width:1200px;height:560px;background:var(--light)}
.origin .photo{position:absolute;left:0;top:0;width:480px;height:500px;background:radial-gradient(ellipse at 35% 45%,#4d8fd6 0%,#8fbbea 40%,#e6eef8 80%,var(--light) 100%)}
.origin-copy{position:absolute;left:520px;top:80px;width:540px}
.origin-copy h2{font-family:"Raleway",sans-serif;font-size:38px;line-height:46px;color:var(--ink)}
.origin-copy h2 b{font-weight:800;display:block}
.origin-copy h2 span{font-weight:400;display:block}
.origin-copy p{font-size:14px;line-height:32px;margin-top:18px}
.btn-outline{display:inline-block;border:2px solid #444;font-family:"Montserrat",sans-serif;font-size:12px;color:#333;padding:8px 17px;margin-top:20px}

/* products */
.products{position:absolute;top:1310px;left:0;width:1200px;height:675px;background:var(--white)}
.section-title{position:absolute;left:0;width:1200px;text-align:center;font-family:"Raleway",sans-serif;font-size:38px;color:var(--ink)}
.section-title b{font-weight:800}
.section-title span{font-weight:400}
.rule{position:absolute;left:567px;width:66px;height:3px}
.product-label{position:absolute;font-size:12px;line-height:20px;color:#666}
.product-label h3{font-family:"Raleway",sans-serif;font-weight:700;font-size:18px;color:#333;margin-bottom:4px}
.product-label.right-al{text-align:right}

/* how we work */
.how{position:absolute;top:1985px;left:0;width:1200px;height:765px;background:linear-gradient(180deg,var(--teal) 0%,#17a9a5 60%,#1bb4ad 100%)}
.how .section-title{color:#fff;top:70px}
.how .lead{position:absolute;top:152px;left:200px;width:800px;text-align:center;color:#eafafa;font-size:14px;line-height:26px}
.step{position:absolute;width:215px;background:#fff;border-radius:108px;text-align:center;padding:38px 14px 0}
.step .icon{width:96px;height:96px;border-radius:50%;background:var(--teal);margin:0 auto;display:flex;align-items:center;justify-content:center}
.step h3{font-family:"Raleway",sans-serif;font-weight:700;font-size:18px;color:#333;margin-top:26px}
.step p{font-size:12px;line-height:24px;color:#666;margin-top:8px}

/* blog */
.blog{position:absolute;top:2750px;left:0;width:1200px;height:700px;background:var(--white)}
.post{position:absolute;top:202px;width:287px}
.post .thumb{height:180px;border-radius:8px;background:linear-gradient(135deg,#c5cfdc 0%,#e8ecf1 45%,#a9b6c6 100%)}
.post .head{display:flex;gap:10px;align-items:flex-start;margin-top:18px}
.post .date{flex:none;width:48px;height:48px;border-radius:50%;border:3px solid var(--green);text-align:center;color:var(--green);font-family:"Montserrat",sans-serif;font-weight:700;font-size:18px;line-height:1;padding-top:8px}
.post .date small{display:block;font-size:8px}
.post h3{font-family:"Raleway",sans-serif;font-weight:400;font-size:17px;line-height:24px;color:#333}
.post p{font-size:12px;line-height:26px;margin-top:10px}
.btn-green{display:inline-block;border:2px solid var(--green);color:var(--green);font-family:"Montserrat",sans-serif;font-size:11px;padding:7px 16px;margin-top:20px}

/* testimonials */
.testimonials{position:absolute;top:3450px;left:0;width:1200px;height:580px;background:linear-gradient(90deg,#f0f2f4 0%,#e6eaee 50%,#f1f3f5 100%)}
.quote{position:absolute;width:276px;background:#fff;text-align:center;padding:78px 20px 26px;font-size:12px;line-height:24px;color:#555;box-shadow:0 4px 14px rgba(0,0,0,.08);border-bottom:8px solid var(--green)}
.quote .mark{position:absolute;top:-32px;left:106px;width:64px;height:64px;border-radius:50%;background:#fff;color:var(--green);font-family:"Raleway",sans-serif;font-weight:800;font-size:56px;line-height:78px}
.quote .who{display:block;font-style:italic;margin-top:14px}

/* footer */
.notch{position:absolute;top:3990px;left:550px;width:100px;height:40px;background:var(--dark);clip-path:polygon(25% 0,75% 0,100% 100%,0 100%)}
.site-footer{position:absolute;top:4030px;left:0;width:1200px;height:365px;background:var(--dark);color:#ddd;font-family:"Montserrat",sans-serif}
.site-footer h4{font-size:16px;font-weight:700;color:#fff;text-transform:uppercase}
.site-footer .col{position:absolute;top:75px}
.site-footer .brand-name{font-size:26px;font-weight:700;color:#fff}
.site-footer p{font-size:13px;line-height:28px}
.contact-row{display:flex;gap:14px;margin-top:18px;font-size:13px;line-height:21px}
.email-field{margin-top:18px;width:276px;height:33px;border-radius:17px;background:#fff;color:#999;font-size:9px;padding:11px 16px}
.subscribe{display:inline-block;margin-top:14px;background:var(--blue);color:#fff;font-size:13px;padding:8px 22px;border-radius:17px}
.bottom-bar{position:absolute;top:4395px;left:0;width:1200px;height:126px;background:var(--darker);border-top:1px solid #222;font-family:"Montserrat",sans-serif;color:#ddd;font-size:13px}
.bottom-bar .copy{position:absolute;left:145px;top:58px}
.bottom-bar .socials{position:absolute;left:913px;top:50px;display:flex;gap:9px}
.bottom-bar .socials span{width:30px;height:30px;border:2px solid var(--blue);border-radius:50%}
</style>
</head>
<body>

<header class="site-header">
  <div class="topbar">
    <div class="item">
      <svg width="13" height="13" viewBox="0 0 24 24"><path fill="#fff" d="M6.6 10.8a15 15 0 0 0 6.6 6.6l2.2-2.2c.3-.3.7-.4 1-.2 1.1.4 2.3.6 3.6.6.6 0 1 .4 1 1V20c0 .6-.4 1-1 1A17 17 0 0 1 3 4c0-.6.4-1 1-1h3.5c.6 0 1 .4 1 1 0 1.3.2 2.5.6 3.6.1.3 0 .7-.2 1z"/></svg>
      Call Us &nbsp;808-4410-2716
    </div>
    <div class="item">
      <svg width="15" height="11" viewBox="0 0 24 18"><path fill="#fff" d="M0 0h24v2L12 10 0 2zM0 4l12 8 12-8v14H0z"/></svg>
      hello@curavel.org
    </div>
    <div class="socials"><span></span><span></span><span></span></div>
  </div>
  <div class="brand"><div class="mark"></div><div class="name">Curavel</div></div>
  <nav class="main-nav">
    <span>HOME</span><span>ABOUT US</span><span>PRODUCTS</span><span>HOW WE WORK</span><span>FAQ</span><span>CONTACT US</span>
  </nav>
</header>

<section class="hero" role="img" aria-label="Photo of a lab technician in mask and cap working at a pharmaceutical production line">
  <div class="hero-copy">
    <div class="pre">WELCOME TO</div>
    <h1>CURAVEL</h1>
    <p>Sed ut perspiciatis unde omnis iste natus sit voluptatem accusantium doloremque laudantium, totam rem aperiam, eaque ipsa</p>
    <span class="btn-blue">GET MORE INFO</span>
  </div>
  <div class="arrow" style="left:63px"><svg width="30" height="30" viewBox="0 0 30 30"><path d="M17 10l-5 5 5 5" stroke="#fff" stroke-width="2.5" fill="none"/></svg></div>
  <div class="arrow" style="left:1104px"><svg width="30" height="30" viewBox="0 0 30 30"><path d="M13 10l5 5-5 5" stroke="#fff" stroke-width="2.5" fill="none"/></svg></div>
</section>

<section class="origin">
  <div class="photo" role="img" aria-label="Spilled bottle of blue gel capsules"></div>
  <div class="origin-copy">
    <h2><b>WHERE ARE YOUR</b><span>DRUGS MADE?</span></h2>
    <p>Prescription drugs sold in the U.S. are manufactured in facilities located all over the world. Many medications you rely on are made in Australia, Canada, China, India, France, Germany, Japan, Malta, Singapore, Sweden, the United Kingdom, and the United States. Unfortunately, if you live in the U.S., and other countries as well, it can be quite the task to pinpoint exactly where your medication was made because companies are not required to list that information.In fact, drug companies are only required to list the corporate headquarters</p>
    <span class="btn-outline">READ MORE</span>
  </div>
</section>
<svg class="hero-bottom-chevron abs" width="30" height="20" viewBox="0 0 30 20"><path d="M4 5l11 10 11-10" stroke="var(--blue)" stroke-width="3" fill="none"/></svg>

<section class="products">
  <h2 class="section-title" style="top:80px"><b>OUR PRODUCTS</b></h2>
  <div class="rule" style="top:140px;background:var(--blue)"></div>
  <svg class="abs" style="left:0;top:0" width="1200" height="675" viewBox="0 1310 1200 675">
    <defs>
      <linearGradient id="inj" x1="0" y1="0" x2="1" y2="1"><stop offset="0" stop-color="#e9eef3"/><stop offset="1" stop-color="#aab6c2"/></linearGradient>
      <linearGradient id="oint" x1="0" y1="0" x2="1" y2="1"><stop offset="0" stop-color="#2b2f36"/><stop offset="1" stop-color="#d8dde3"/></linearGradient>
      <linearGradient id="syr" x1="0" y1="0" x2="1" y2="1"><stop offset="0" stop-color="#f2e6c9"/><stop offset="1" stop-color="#8a3b12"/></linearGradient>
      <linearGradient id="cap" x1="0" y1="0" x2="1" y2="1"><stop offset="0" stop-color="#f6c22b"/><stop offset="1" stop-color="#c48507"/></linearGradient>
      <linearGradient id="herb" x1="0" y1="0" x2="1" y2="1"><stop offset="0" stop-color="#6d9b3a"/><stop offset="1" stop-color="#c9925a"/></linearGradient>
      <linearGradient id="lab" x1="0" y1="0" x2="1" y2="1"><stop offset="0" stop-color="#c98a5a"/><stop offset=".5" stop-color="#e9e2da"/><stop offset="1" stop-color="#b77b4f"/></linearGradient>
    </defs>
    <g stroke="var(--blue)" stroke-width="2" fill="none">
      <path d="M381 1985 A 255 255 0 0 1 817 1985"/>
      <path d="M381 1985 A 240 240 0 0 1 381 1890"/>
      <line x1="610" y1="1646" x2="610" y2="1703"/>
      <line x1="405" y1="1700" x2="467" y2="1745"/>
      <line x1="793" y1="1700" x2="728" y2="1745"/>
      <line x1="312" y1="1846" x2="381" y2="1893"/>
      <line x1="886" y1="1846" x2="817" y2="1893"/>
    </g>
    <g fill="#fff" stroke="var(--blue)" stroke-width="2">
      <circle cx="610" cy="1703" r="7"/><circle cx="467" cy="1745" r="7"/><circle cx="728" cy="1745" r="7"/>
      <circle cx="381" cy="1893" r="7"/><circle cx="817" cy="1893" r="7"/>
    </g>
    <g stroke="var(--blue)" stroke-width="4">
      <circle cx="610" cy="1584" r="62" fill="url(#inj)" role="img" aria-label="Syringe and vial"/>
      <circle cx="361" cy="1666" r="62" fill="url(#oint)" role="img" aria-label="Ointment tubes"/>
      <circle cx="837" cy="1666" r="62" fill="url(#syr)" role="img" aria-label="Syrup poured into spoon"/>
      <circle cx="277" cy="1812" r="62" fill="url(#cap)" role="img" aria-label="Yellow soft capsules"/>
      <circle cx="921" cy="1812" r="62" fill="url(#herb)" role="img" aria-label="Herbal remedies and leaves"/>
    </g>
    <clipPath id="cut"><rect x="0" y="1310" width="1200" height="675"/></clipPath>
    <circle cx="600" cy="1935" r="210" fill="url(#lab)" clip-path="url(#cut)" role="img" aria-label="Worker in lab coat checking boxes in a warehouse"/>
  </svg>
  <div class="product-label right-al" style="left:340px;top:198px;width:185px"><h3>Injections</h3>Nemo enim ipsam<br>voluptatem quia voluptas</div>
  <div class="product-label right-al" style="left:88px;top:334px;width:185px"><h3>Ointment</h3>Nemo enim ipsam<br>voluptatem quia voluptas</div>
  <div class="product-label right-al" style="left:5px;top:472px;width:185px"><h3>Capsules</h3>Nemo enim ipsam<br>voluptatem quia voluptas</div>
  <div class="product-label" style="left:928px;top:318px"><h3>Syrup</h3>Nemo enim ipsam<br>voluptatem quia voluptas</div>
  <div class="product-label" style="left:1007px;top:462px"><h3>Herbal</h3>Nemo enim ipsam<br>voluptatem quia voluptas</div>
</section>

<section class="how">
  <h2 class="section-title"><b>HOW WE WORK</b></h2>
  <div class="rule" style="top:135px;background:#fff;width:56px;left:572px"></div>
  <p class="lead">Sed ut perspiciatis unde omnis iste natus error sit voluptatem accusantium doloremque laudantium, totam rem aperiam, eaque ipsa quae ab illo inventore veritatis et quasi architecto beatae</p>

  <div class="step" style="left:143px;top:327px;height:351px">
    <div class="icon"><svg width="40" height="44" viewBox="0 0 40 44"><path d="M12 14v-4a8 8 0 0 1 16 0v4" stroke="#fff" stroke-width="3" fill="none"/><rect x="4" y="14" width="32" height="28" rx="4" fill="#fff"/></svg></div>
    <h3>HOW WE SHIP</h3>
    <p>Sed ut perspiciatis unde omnis iste natus error sit voluptatem accusantium doloremque laium, totam rem aperiam, eaque ipsa quae</p>
  </div>
  <div class="step" style="left:377px;top:253px;height:351px">
    <div class="icon"><svg width="46" height="46" viewBox="0 0 46 46"><path d="M6 6h16l18 18-16 16L6 22z" fill="#fff"/><circle cx="14" cy="14" r="3" fill="var(--teal)"/></svg></div>
    <h3>MINIMUM ORDERS</h3>
    <p>Sed ut perspiciatis unde omnis iste natus error sit voluptatem accusantium doloremque laium, totam rem aperiam, eaque ipsa quae</p>
  </div>
  <div class="step" style="left:610px;top:327px;height:351px">
    <div class="icon"><svg width="34" height="42" viewBox="0 0 34 42"><path d="M2 2h20l10 10v28H2z" fill="#fff"/><g stroke="var(--teal)" stroke-width="2.5"><line x1="9" y1="20" x2="25" y2="20"/><line x1="9" y1="26" x2="25" y2="26"/><line x1="9" y1="32" x2="25" y2="32"/></g></svg></div>
    <h3>CREDIT TERMS</h3>
    <p>Sed ut perspiciatis unde omnis iste natus error sit voluptatem accusantium doloremque laium, totam rem aperiam, eaque ipsa quae</p>
  </div>
  <div class="step" style="left:843px;top:253px;height:351px">
    <div class="icon"><svg width="46" height="34" viewBox="0 0 46 34"><rect x="1" y="1" width="44" height="32" rx="4" fill="#fff"/><rect x="1" y="9" width="44" height="6" fill="var(--teal)"/><rect x="7" y="22" width="14" height="4" fill="var(--teal)"/></svg></div>
    <h3>PAYMENT TYPES..</h3>
    <p>Sed ut perspiciatis unde omnis iste natus error sit voluptatem accusantium doloremque laium, totam rem aperiam, eaque ipsa quae</p>
  </div>
</section>

<section class="blog">
  <h2 class="section-title" style="top:80px"><b>FROM</b> <span>THE BLOG</span></h2>
  <div class="rule" style="top:145px;background:var(--green)"></div>
  <article class="post" style="left:144px">
    <div class="thumb" role="img" aria-label="Lab worker inspecting a packaging line"></div>
    <div class="head"><div class="date">02<small>FEB</small></div><h3>Sed ut perspiciatis unde iste natus sit volup</h3></div>
    <p>Sed ut perspiciatis unde omnis iste natus sit voluptatem accusantium doloremque laudium, totam rem aperiam, eaque ipsa quae</p>
    <span class="btn-green">READ MORE</span>
  </article>
  <article class="post" style="left:456px">
    <div class="thumb" role="img" aria-label="Worker in lab coat using a tablet"></div>
    <div class="head"><div class="date">02<small>FEB</small></div><h3>Sed ut perspiciatis unde iste natus sit volup</h3></div>
    <p>Sed ut perspiciatis unde omnis iste natus sit voluptatem accusantium doloremque laudium, totam rem aperiam, eaque ipsa quae</p>
    <span class="btn-green">READ MORE</span>
  </article>
  <article class="post" style="left:768px">
    <div class="thumb" role="img" aria-label="Two workers in protective suits checking cartons"></div>
    <div class="head"><div class="date">02<small>FEB</small></div><h3>Sed ut perspiciatis unde iste natus sit volup</h3></div>
    <p>Sed ut perspiciatis unde omnis iste natus sit voluptatem accusantium doloremque laudium, totam rem aperiam, eaque ipsa quae</p>
    <span class="btn-green">READ MORE</span>
  </article>
</section>

<section class="testimonials" role="img" aria-label="Faded background photo of a lab technician">
  <h2 class="section-title" style="top:65px"><b>TESTIMONIALS</b></h2>
  <div class="quote" style="left:144px;top:183px"><span class="mark">&ldquo;</span>Sed ut perspiciatis unde omnis iste natus error sit voluptatem accusantium doloremque laudantium, totam rem aperiam, eaque ipsa quae ab illo inventore veritatis et quasi architecto<span class="who">- Varenko, L.</span></div>
  <div class="quote" style="left:462px;top:220px"><span class="mark">&ldquo;</span>Sed ut perspiciatis unde omnis iste natus error sit voluptatem accusantium doloremque laudantium, totam rem aperiam, eaque ipsa quae ab illo inventore veritatis et quasi architecto<span class="who">- Varenko, L.</span></div>
  <div class="quote" style="left:780px;top:183px"><span class="mark">&ldquo;</span>Sed ut perspiciatis unde omnis iste natus error sit voluptatem accusantium doloremque laudantium, totam rem aperiam, eaque ipsa quae ab illo inventore veritatis et quasi architecto<span class="who">- Varenko, L.</span></div>
</section>

<div class="notch"></div>
<svg class="abs" style="left:585px;top:4000px" width="30" height="20" viewBox="0 0 30 20"><path d="M4 15l11-10 11 10" stroke="#fff" stroke-width="3" fill="none"/></svg>

<footer class="site-footer">
  <div class="col" style="left:143px;width:300px;top:70px">
    <div class="brand-name">Curavel</div>
    <p style="margin-top:18px">Sed ut perspiciatis unde omnis iste natus error sit voluptatem accusantium doloremque latium, totam rem aperiam, eaque ipsa quae ab illo inventore vetatis et quasi architecto totam rem aperiam</p>
  </div>
  <div class="col" style="left:493px">
    <h4>Contact Us</h4>
    <div class="contact-row"><svg width="14" height="18" viewBox="0 0 14 18"><path d="M7 1a6 6 0 0 0-6 6c0 4.5 6 10 6 10s6-5.5 6-10a6 6 0 0 0-6-6z" stroke="#ddd" stroke-width="1.5" fill="none"/><circle cx="7" cy="7" r="2" fill="#ddd"/></svg><div>Curavel<br>218 Linden Crest Ave, Ste 40,<br>Marlow TX 75210</div></div>
    <div class="contact-row"><svg width="14" height="14" viewBox="0 0 24 24"><path fill="none" stroke="#ddd" stroke-width="2" d="M6.6 10.8a15 15 0 0 0 6.6 6.6l2.2-2.2c.3-.3.7-.4 1-.2 1.1.4 2.3.6 3.6.6.6 0 1 .4 1 1V20c0 .6-.4 1-1 1A17 17 0 0 1 3 4c0-.6.4-1 1-1h3.5c.6 0 1 .4 1 1 0 1.3.2 2.5.6 3.6.1.3 0 .7-.2 1z"/></svg><div>Phone:<br>1-888-402-6150</div></div>
    <div class="contact-row"><svg width="15" height="12" viewBox="0 0 24 18"><rect x="1" y="1" width="22" height="16" stroke="#ddd" stroke-width="2" fill="none"/><path d="M1 1l11 9 11-9" stroke="#ddd" stroke-width="2" fill="none"/></svg><div>Email:<br>hello@curavel.org</div></div>
  </div>
  <div class="col" style="left:781px;width:280px">
    <h4>Sign up to receive email</h4>
    <p style="font-size:11px;line-height:22px;margin-top:14px">Excepteur sint occaecat cupidatat non proident, sunt in culpa qui Nemo</p>
    <div class="email-field">Enter Email</div>
    <span class="subscribe">Subscribe</span>
  </div>
</footer>

<div class="bottom-bar">
  <div class="copy">Copyright &copy; Curavel 2019. All rights reserved. | Privacy Policy</div>
  <div class="socials"><span></span><span></span><span></span><span></span></div>
</div>

</body>
</html>
```